Excel Template (Branded)

I have a number of reports that I create in Excel. I would like them to be branded instead of generic. Creating a template that I could use for all of my reports would be ideal. I would like to use the colours and logo of my website quillborne.ca for branding ideas.

Target Market(s)

Everyday investors over the age of 18

Industry/Entity Type

investment

Requirements
Must have
• Professional design that will be shared with readers and subscribers of my blog
Nice to have
• clean professional design elements

```html
<!DOCTYPE html>
<html lang="en">
<head>
<meta charset="utf-8">
<title>Quillborne – 10YR Compound Annual Growth Rates</title>
<link rel="stylesheet" href="https://fonts.googleapis.com/css2?family=Ubuntu:wght@500;700&display=swap">
<style>
  :root{
    --navy-1:#1d365f;
    --navy-2:#2f5a94;
    --navy-dark:#1c2a45;
    --navy-mid:#2b4470;
    --blue-head:#4f81bd;
    --row-a:#b8cce4;
    --row-b:#dce6f1;
    --green-top:#0f9150;
    --green-bottom:#0a6a1c;
    --brand-green:#0f9150;
    --brand-blue:#35507e;
    --white:#ffffff;
  }
  *{box-sizing:border-box;margin:0;padding:0}
  html,body{width:1200px;height:692px;overflow:hidden;background:var(--white)}
  body{font-family:"Ubuntu",sans-serif;position:relative;color:var(--white)}

  .brand{position:absolute;left:10px;top:22px;display:flex;align-items:center;gap:8px}
  .brand-mark{width:40px;height:40px;border-radius:50%;background:var(--brand-green)}
  .brand-name{font-weight:700;font-size:30px;color:var(--brand-blue);letter-spacing:-.5px}

  .title-bar{position:absolute;left:217px;top:0;width:967px;height:50px;
    background:linear-gradient(90deg,var(--navy-1),var(--navy-2));
    border:2px solid #6f9bd6;border-top:none;border-radius:0 0 10px 10px;
    display:flex;align-items:center;justify-content:center;
    font-weight:700;font-size:23px}

  .section-band{position:absolute;left:215px;top:58px;width:985px;height:44px;
    background:linear-gradient(180deg,var(--green-top),var(--green-bottom))}
  .section-label{position:absolute;top:0;height:44px;display:flex;align-items:center;gap:10px;
    font-weight:700;font-size:17px}
  .section-dividers{position:absolute;left:0;top:58px}

  .cagr-tab{position:absolute;top:108px;height:15px;width:54px;background:var(--navy-dark);
    font-weight:700;font-size:10.5px;display:flex;align-items:center;justify-content:center;
    clip-path:polygon(0 0,88% 0,100% 40%,100% 100%,0 100%)}

  .grid{position:absolute;left:0;width:1200px;display:grid;
    grid-template-columns:56px 155px repeat(17,55px) 54px}
  .grid-head{top:127px;height:21px}
  .grid-head div{background:var(--blue-head);border-right:1px solid #dfe8f3;
    font-weight:700;font-size:9.5px;display:flex;align-items:center;justify-content:center}
  .grid-head .company{justify-content:flex-start;padding-left:3px;font-size:12.5px}
  .grid-head .price{background:var(--navy-mid)}
  .grid-head .metric{background:var(--navy-dark)}
  .grid-body{top:148px;height:399px;
    background:repeating-linear-gradient(180deg,
      var(--row-a) 0 17.15px,var(--white) 17.15px 18.15px,
      var(--row-b) 18.15px 35.3px,var(--white) 35.3px 36.3px)}
  .grid-body div{border-right:1px solid var(--white)}

  .averages{position:absolute;left:211px;top:556px;width:657px;height:29px;
    background:linear-gradient(180deg,var(--green-top),var(--green-bottom));
    clip-path:polygon(0 0,98.6% 0,100% 30%,100% 100%,0 100%);
    display:flex;align-items:center;justify-content:center;font-weight:700;font-size:19px}
  .average-cells{position:absolute;left:869px;top:556px;width:331px;height:30px;display:flex}
  .average-cells div{flex:0 0 55px;height:100%;border-right:1px solid var(--white);
    background:linear-gradient(180deg,var(--green-top),var(--green-bottom))}
  .average-cells div:first-child{flex-basis:57px}
  .average-cells div:last-child{flex-basis:54px;border-right:none}

  .note{position:absolute;left:0;top:609px;width:868px;height:83px;padding:5px 6px;
    background:linear-gradient(180deg,var(--green-top),var(--green-bottom));
    font-weight:700;font-size:13.4px;line-height:19px}
</style>
</head>
<body>
  <div class="brand">
    <span class="brand-mark"></span>
    <span class="brand-name">Quillborne</span>
  </div>

  <header class="title-bar">10YR-Compound Annual Growth Rates (CAGR) as of 01-01-2021</header>

  <div class="section-band">
    <div class="section-label" style="left:86px">Ten Years of Dividend Growth (Year-by-Year)
      <svg width="26" height="34" viewBox="0 0 26 34" fill="none" stroke="#fff" stroke-width="2">
        <text x="7" y="12" fill="#fff" stroke="none" font-size="14" font-weight="700" font-family="Ubuntu,sans-serif">$</text>
        <path d="M13 15v13M13 22c-4-1-7-4-8-7 4 0 7 3 8 7zM13 22c4-1 7-4 8-7-4 0-7 3-8 7z"/>
        <path d="M5 29h16v3H5z" fill="#fff"/>
      </svg>
    </div>
    <div class="section-label" style="left:558px">Price
      <svg width="32" height="32" viewBox="0 0 32 32" fill="none" stroke="#fff" stroke-width="2">
        <circle cx="16" cy="16" r="14"/><circle cx="16" cy="16" r="9"/>
        <text x="11" y="21" fill="#fff" stroke="none" font-size="14" font-weight="700" font-family="Ubuntu,sans-serif">$</text>
      </svg>
    </div>
    <div class="section-label" style="left:707px">Yield
      <svg width="32" height="32" viewBox="0 0 32 32" fill="none" stroke="#fff" stroke-width="2">
        <circle cx="16" cy="16" r="14"/>
        <path d="M11 22v-4M15 22v-7M19 22v-9M10 14l9-5M16 9h3v3"/>
      </svg>
    </div>
    <div class="section-label" style="left:891px">Total return
      <svg width="30" height="30" viewBox="0 0 30 30" fill="none" stroke="#fff" stroke-width="2.4">
        <path d="M6 15a10 10 0 1 0 3-7"/><path d="M3 13l4 5 4-4z" fill="#fff"/>
      </svg>
    </div>
  </div>
  <svg class="section-dividers" width="1200" height="44" viewBox="0 0 1200 44" fill="none" stroke="#fff" stroke-width="2">
    <path d="M746 0l16 14v30M855 0l16 14v30M1020 0l16 14v30M1184 0l16 14"/>
  </svg>

  <div class="cagr-tab" style="left:1037px">CAGR</div>
  <div class="cagr-tab" style="left:1092px">CAGR</div>
  <div class="cagr-tab" style="left:1147px">CAGR</div>

  <div class="grid grid-head">
    <div>Symbol</div><div class="company">Company</div>
    <div>2011</div><div>2012</div><div>2013</div><div>2014</div><div>2015</div>
    <div>2016</div><div>2017</div><div>2018</div><div>2019</div><div>2020</div>
    <div class="price">$'11</div><div class="price">$'21</div>
    <div class="metric">YLD'11</div><div class="metric">YLD'21</div><div class="metric">10YOC</div>
    <div class="metric">10Y TR</div><div class="metric">10Y DG</div><div class="metric">10Y PG</div>
  </div>

  <div class="grid grid-body">
    <div></div><div></div><div></div><div></div><div></div><div></div><div></div>
    <div></div><div></div><div></div><div></div><div></div><div></div><div></div>
    <div></div><div></div><div></div><div></div><div></div><div></div>
  </div>

  <div class="averages">Averages</div>
  <div class="average-cells"><div></div><div></div><div></div><div></div><div></div><div></div></div>

  <p class="note">As successful dividend growth investors we understand that rising dividends are a foundation for higher share prices.<br>
  Here is the Compound Annual Growth Rate (CAGR) of dividends and CAGR of price over the last decade so that you can study<br>
  the evidence that as the dividend grows, so does the price</p>
</body>
</html>
```